Criminal Defense Firm looking for an edge in business card design

Established Criminal Defense Firm looking to refresh business card. We already have logo and website, but our business cards are extremely boring. We would like to also have something on the backside of card.
Needs to be business oriented, but creative.
We provide services to professionals such as doctors, lawyers, politicians, etc.
Our specialty is to protect professional licenses when facing a criminal matter.

Update on March 10, 2015: This project is for a Business Card Design. The winner in this project will be assigned the next (1on1) project which incidentally is also entitled Business Card Design. I'm sorry for this confusion. The 1on1 project will not be for Business Card Design but will be for Stationery-Envelope Design. Thank you for your attention and continued participation.

Target Market(s)

People accused of a crime

Industry/Entity Type

Business

Contact Information for Business Card

Simple, strong, professional

Colors
85abd2
3176b5
0355a3

```html
<!DOCTYPE html>
<html lang="en">
<head>
<meta charset="utf-8">
<title>Whitcombe Ashford Law Corporation – Business Cards</title>
<link rel="stylesheet" href="https://fonts.googleapis.com/css2?family=Cardo:wght@400;700&display=swap">
<style>
  :root {
    --page-bg: #e8e5e0;
    --card-white: #ffffff;
    --brand-blue: #4f93b8;
    --card-blue: #5799bb;
    --ink-dark: #1b1b1b;
    --ink-grey: #555a5e;
    --on-blue: #ffffff;
    --shadow: rgba(0, 0, 0, 0.18);
  }
  * { box-sizing: border-box; margin: 0; padding: 0; }
  html, body {
    width: 1200px;
    height: 1000px;
    overflow: hidden;
    background: var(--page-bg);
    font-family: "Cardo", Georgia, serif;
  }
  .card {
    position: absolute;
    width: 525px;
    height: 300px;
    overflow: hidden;
    box-shadow: 0 6px 18px var(--shadow);
  }

  /* Front */
  .card-front {
    left: 90px;
    top: 230px;
    background: var(--card-white);
  }
  .holder-name {
    position: absolute;
    left: 34px;
    top: 26px;
    font-size: 31px;
    font-weight: 700;
    color: var(--ink-dark);
    line-height: 1;
  }
  .holder-name .first { color: var(--brand-blue); }
  .holder-title {
    position: absolute;
    left: 92px;
    top: 60px;
    font-size: 15px;
    color: var(--ink-grey);
  }
  .contact-list {
    position: absolute;
    left: 38px;
    top: 100px;
    list-style: none;
    font-size: 17px;
    color: var(--ink-grey);
    line-height: 1.2;
  }
  .contact-item {
    display: flex;
    align-items: flex-start;
    gap: 12px;
    margin-bottom: 15px;
  }
  .contact-icon {
    width: 22px;
    height: 22px;
    flex: none;
    fill: var(--brand-blue);
  }
  .brand-ring {
    position: absolute;
    left: 385px;
    top: 28px;
    width: 250px;
    height: 250px;
    border: 8px solid var(--brand-blue);
    border-radius: 50%;
  }
  .brand-name-front {
    position: absolute;
    left: 400px;
    top: 122px;
    width: 120px;
    text-align: center;
    font-size: 21px;
    font-weight: 700;
    line-height: 1.15;
    color: var(--brand-blue);
  }

  /* Back */
  .card-back {
    left: 585px;
    top: 500px;
    background: var(--card-blue);
  }
  .back-brand {
    position: absolute;
    left: 52px;
    top: 70px;
    display: flex;
    align-items: center;
    gap: 18px;
  }
  .back-mark {
    width: 62px;
    height: 62px;
    border: 3px solid var(--on-blue);
    border-radius: 50%;
    flex: none;
  }
  .back-name {
    color: var(--on-blue);
    font-weight: 400;
    font-size: 24px;
    letter-spacing: 1.5px;
    text-transform: uppercase;
    line-height: 1.05;
  }
  .back-name .suffix {
    display: block;
    text-transform: none;
    letter-spacing: 0.5px;
    font-size: 16px;
    margin-top: 4px;
    padding-left: 140px;
  }
</style>
</head>
<body>

<section class="card card-front" aria-label="Business card front">
  <h1 class="holder-name"><span class="first">Dana</span> Whitcombe</h1>
  <p class="holder-title">Attorney at Law</p>

  <ul class="contact-list">
    <li class="contact-item">
      <svg class="contact-icon" viewBox="0 0 24 24" aria-hidden="true"><path d="M2 6h20v12H2z M2 6l10 7 10-7" fill="var(--brand-blue)"/><path d="M3 7l9 6.3L21 7" fill="none" stroke="#fff" stroke-width="1.6"/></svg>
      <span>dana@wacounsel.com</span>
    </li>
    <li class="contact-item">
      <svg class="contact-icon" viewBox="0 0 24 24" aria-hidden="true"><path d="M12 2a7 7 0 0 0-7 7c0 5 7 13 7 13s7-8 7-13a7 7 0 0 0-7-7zm0 9.5A2.5 2.5 0 1 1 12 6.5a2.5 2.5 0 0 1 0 5z"/></svg>
      <span>1180 Meridian Avenue, Suite 210<br>Riverton, California 93799</span>
    </li>
    <li class="contact-item">
      <svg class="contact-icon" viewBox="0 0 24 24" aria-hidden="true"><path d="M6.6 10.8a15 15 0 0 0 6.6 6.6l2.2-2.2a1 1 0 0 1 1-.25 11.4 11.4 0 0 0 3.6.57 1 1 0 0 1 1 1V20a1 1 0 0 1-1 1A17 17 0 0 1 3 4a1 1 0 0 1 1-1h3.5a1 1 0 0 1 1 1 11.4 11.4 0 0 0 .57 3.6 1 1 0 0 1-.25 1z"/></svg>
      <span>555.014.2200</span>
    </li>
    <li class="contact-item">
      <svg class="contact-icon" viewBox="0 0 24 24" aria-hidden="true"><path d="M7 3h8l3 3v4H7z M4 10h16a2 2 0 0 1 2 2v6h-4v3H6v-3H2v-6a2 2 0 0 1 2-2z M8 16v3h8v-3z"/></svg>
      <span>555.014.2201</span>
    </li>
  </ul>

  <div class="brand-ring" aria-hidden="true"></div>
  <p class="brand-name-front">Whitcombe<br>Ashford</p>
</section>

<section class="card card-back" aria-label="Business card back">
  <div class="back-brand">
    <div class="back-mark" aria-hidden="true"></div>
    <p class="back-name">Whitcombe<br>Ashford<span class="suffix">Law Corporation</span></p>
  </div>
</section>

</body>
</html>
```